Business Card Design - Construction Company

Tarrowin Construction is in need of a sharp, modern business card design that has an architectural/high fashion feel.

We are looking for a two sided card.

One side simple dark grey/black with some texture in the background. e.g. (a mosaic of simple interconnecting shapes or a shadow of the logo.) Something to draw attention and create interest.It will need to feature a large Tarrowin construction logo (files attached) in metallic gradient or plain white.

The other side should contain all of our information:

(in largest text)
Name of person
Tarrowin Construction Pty. Ltd.

Licensed builders specialising in:
- Bathrooms
- Kitchens
- Commercial interiors

(mid sized text)
Phone number
Fax number
person@tarrowinconstruction.example.au
www. tarrowinconstruction.example.au

(smaller text)
ABN: 62407938215
BSA license: xxx-xxxx
PO Box 8641 Kellsmoor QLD 4019 (address)

Target Market(s)

professional home and business owners

Industry/Entity Type

Construction

Requirements
Must have
• Must be bold, professional looking and modern.
Nice to have
• We are undecided as to what kind of printing we will go with.
Definitely square edged.
Probably high quality satin card.
We are also interested in designs that would work well on transparent or translucent plastic.
Ideally we would print two versions.
Should not have
• Nothing with an antique feel.
No wild colours. Small amounts of colour can be good in the right place.

```html
<!DOCTYPE html>
<html lang="en">
<head>
<meta charset="utf-8">
<title>Tarrowin Construction — Business Cards</title>
<link rel="stylesheet" href="https://fonts.googleapis.com/css2?family=Play:wght@400;700&display=swap">
<style>
  :root {
    --backdrop: #4a4a4a;
    --card: #050505;
    --ink: #ffffff;
    --ink-soft: #d6d6d6;
    --ink-dim: #9a9a9a;
    --mark: #c9c9c9;
    --ghost: rgba(255,255,255,0.07);
  }
  * { margin: 0; padding: 0; box-sizing: border-box; }
  html, body { width: 1200px; height: 900px; overflow: hidden; }
  body {
    background: var(--backdrop);
    font-family: "Play", sans-serif;
    color: var(--ink);
    position: relative;
  }
  .card {
    position: absolute;
    background: var(--card);
    overflow: hidden;
    box-shadow: 0 4px 14px rgba(0,0,0,0.45);
  }
  .card--info-a { left: 10px;  top: 94px;  width: 522px; height: 282px; }
  .card--info-b { left: 593px; top: 92px;  width: 522px; height: 286px; }
  .card--brand-a { left: 30px;  top: 528px; width: 446px; height: 245px; }
  .card--brand-b { left: 562px; top: 528px; width: 445px; height: 245px; }

  .brand { position: absolute; text-align: center; color: var(--mark); font-weight: 700; white-space: nowrap; }
  .brand__dot { display: block; margin: 0 auto; border-radius: 50%; border: 3px solid var(--mark); }
  .brand__name { display: block; letter-spacing: 1px; line-height: 1; }

  .card--info-a .brand, .card--info-b .brand { left: 55px; top: 84px; width: 170px; }
  .card--info-a .brand__dot, .card--info-b .brand__dot { width: 52px; height: 52px; margin-bottom: 14px; }
  .card--info-a .brand__name, .card--info-b .brand__name { font-size: 20px; }
  .card--info-a .brand__sub, .card--info-b .brand__sub { font-size: 7.5px; letter-spacing: 1.5px; margin-top: 3px; }

  .card--brand-a .brand, .card--brand-b .brand { left: 0; right: 0; top: 42px; }
  .card--brand-a .brand__dot, .card--brand-b .brand__dot { width: 82px; height: 82px; border-width: 5px; margin-bottom: 18px; }
  .card--brand-a .brand__name, .card--brand-b .brand__name { font-size: 42px; letter-spacing: 3px; }
  .card--brand-a .brand__sub, .card--brand-b .brand__sub { font-size: 16px; letter-spacing: 5px; margin-top: 4px; }

  .ghost-ring {
    position: absolute; right: -30px; top: 90px;
    width: 180px; height: 180px; border-radius: 50%;
    border: 20px solid var(--ghost);
  }

  .person { position: absolute; left: 252px; top: 58px; font-size: 21px; font-weight: 700; white-space: nowrap; }
  .contact { position: absolute; left: 252px; top: 98px; list-style: none; font-size: 11px; color: var(--ink-soft); white-space: nowrap; }
  .contact li { display: flex; align-items: center; height: 18px; }
  .contact li.contact__phone { font-size: 12.5px; }
  .contact svg { width: 14px; height: 12px; margin-right: 10px; flex: none; fill: none; stroke: var(--ink-soft); stroke-width: 1.3; }
  .legal { position: absolute; left: 252px; top: 192px; font-size: 9px; color: var(--ink-dim); line-height: 13px; white-space: nowrap; }

  .services { position: absolute; left: 0; right: 0; bottom: 10px; height: 14px; font-size: 10.5px; white-space: nowrap; }
  .services span { position: absolute; top: 0; }
  .services__lead { left: 30px; color: var(--ink-dim); }
  .services__item { color: var(--ink); }
  .services__item--bath { left: 233px; }
  .services__item--kitchen { left: 320px; }
  .services__item--interior { left: 387px; }
</style>
</head>
<body>

<svg width="0" height="0" style="position:absolute" aria-hidden="true">
  <symbol id="i-home" viewBox="0 0 15 13"><path d="M1 6.5 7.5 1 14 6.5M3 5.5V12h9V5.5"/></symbol>
  <symbol id="i-mail" viewBox="0 0 15 13"><rect x="1" y="2.5" width="13" height="8"/><path d="M1 2.5 7.5 7 14 2.5"/></symbol>
  <symbol id="i-web" viewBox="0 0 15 13"><circle cx="7.5" cy="6.5" r="5.7"/><path d="M4.5 4.5 6 9l1.5-3.5L9 9l1.5-4.5"/></symbol>
  <symbol id="i-phone" viewBox="0 0 15 13"><path d="M1.5 4.5c0-2 2.5-3 6-3s6 1 6 3H10V3.5H5v1Z"/><rect x="3.5" y="6" width="8" height="5.5"/></symbol>
  <symbol id="i-fax" viewBox="0 0 15 13"><rect x="1" y="5" width="13" height="6.5"/><path d="M4 5V1.5h7V5M4 8.5h7"/></symbol>
</svg>

<section class="card card--info-a" aria-label="Card back, version one">
  <div class="ghost-ring"></div>
  <div class="brand"><span class="brand__dot"></span><span class="brand__name">TARROWIN</span><span class="brand__name brand__sub">CONSTRUCTION</span></div>
  <h1 class="person">Your Name Here</h1>
  <ul class="contact">
    <li><svg><use href="#i-home"/></svg>PO Box 8641 Kellsmoor QLD 4019</li>
    <li><svg><use href="#i-mail"/></svg>person@tarrowinconstruction.example.au</li>
    <li><svg><use href="#i-web"/></svg>www.tarrowinconstruction.example.au</li>
    <li class="contact__phone"><svg><use href="#i-phone"/></svg>555 018 246</li>
    <li class="contact__phone"><svg><use href="#i-fax"/></svg>555 018 397</li>
  </ul>
  <p class="legal">BSA license: xxx-xxxx<br>ABN: 62407938215</p>
  <p class="services"><span class="services__lead">Licensed builders specialising in</span><span class="services__item services__item--bath">Bathrooms</span><span class="services__item services__item--kitchen">Kitchens</span><span class="services__item services__item--interior">Commercial Interiors</span></p>
</section>

<section class="card card--info-b" aria-label="Card back, version two">
  <div class="brand"><span class="brand__dot"></span><span class="brand__name">TARROWIN</span><span class="brand__name brand__sub">CONSTRUCTION</span></div>
  <h1 class="person">Your Name Here</h1>
  <ul class="contact">
    <li><svg><use href="#i-home"/></svg>PO Box 8641 Kellsmoor QLD 4019</li>
    <li><svg><use href="#i-mail"/></svg>person@tarrowinconstruction.example.au</li>
    <li><svg><use href="#i-web"/></svg>www.tarrowinconstruction.example.au</li>
    <li class="contact__phone"><svg><use href="#i-phone"/></svg>555 018 246</li>
    <li class="contact__phone"><svg><use href="#i-fax"/></svg>555 018 397</li>
  </ul>
  <p class="legal">BSA license: xxx-xxxx<br>ABN: 62407938215</p>
  <p class="services"><span class="services__lead">Licensed builders specialising in</span><span class="services__item services__item--bath">Bathrooms</span><span class="services__item services__item--kitchen">Kitchens</span><span class="services__item services__item--interior">Commercial Interiors</span></p>
</section>

<section class="card card--brand-a" aria-label="Card front, version one">
  <div class="brand"><span class="brand__dot"></span><span class="brand__name">TARROWIN</span><span class="brand__name brand__sub">CONSTRUCTION</span></div>
</section>

<section class="card card--brand-b" aria-label="Card front, version two">
  <div class="brand"><span class="brand__dot"></span><span class="brand__name">TARROWIN</span><span class="brand__name brand__sub">CONSTRUCTION</span></div>
</section>

</body>
</html>
```